Business Card Design Project

New Business Card design for Varodine Technology Ltd using new Logo and new Tagline for staffing company.

About us from our website - www.varodine.example:

VaroDine is a leading and recognized Electronic Entertainment, Workforce Augmentation, and Project Management solutions provider with clients in Electronic Entertainment, Legal, Technology, Government and other verticals that range in size from start up organizations to Zenlar 500 companies. VaroDine is certified as an 8(a) minority and woman owned enterprise, established in 1998.

Target Market(s)

Companies in Electronic Entertainment, Legal, Government and Technology

Industry/Entity Type

Business

Requirements
Must have
• Must include in small letters the following information on back:

Established in 1998
8(a)(w)(e), Cage #7KRT9, DUNS #462137580

Front should have the following:
Derek Holloway
Vice President
5820 Birchmont Road
Fallowby, FB 482917
555-318-2746 X 100
555-902-6613 Fax
555-318-2746 Toll Free
name@varodine.example

Our Tagline: Connect • Collaborate • Achieve

```html
<!DOCTYPE html>
<html lang="en">
<head>
<meta charset="utf-8">
<title>VaroDine Business Card</title>
<link href="https://fonts.googleapis.com/css2?family=Arimo:wght@400;700&display=swap" rel="stylesheet">
<style>
  :root {
    --canvas: #d9d9d9;
    --blue-light: #0b74c0;
    --blue-mid: #0a4fa0;
    --blue-deep: #0d2f7a;
    --blue-text: #0b5cb0;
    --ink: #2b2b2b;
    --logo-grey: #555a60;
    --lavender: #c9cdec;
    --fold-grey: #e2e2e2;
    --white: #ffffff;
  }
  * { margin: 0; padding: 0; box-sizing: border-box; }
  html, body { width: 1200px; height: 900px; overflow: hidden; }
  body {
    background: var(--canvas);
    font-family: "Arimo", Arial, sans-serif;
    position: relative;
  }
  .card {
    position: absolute;
    width: 530px;
    height: 320px;
    overflow: hidden;
    box-shadow: 0 4px 12px rgba(0,0,0,0.25);
  }
  .card-back {
    left: 190px; top: 115px;
    background: radial-gradient(circle at 30% 25%, var(--blue-light) 0%, var(--blue-mid) 55%, var(--blue-deep) 100%);
  }
  .card-front { left: 518px; top: 455px; background: var(--white); }
  .card-decor { position: absolute; inset: 0; width: 100%; height: 100%; }

  .wordmark {
    position: absolute;
    display: flex;
    align-items: center;
    gap: 10px;
    font-weight: 700;
    letter-spacing: -1px;
  }
  .wordmark-dot { border-radius: 50%; flex: none; }
  .card-back .wordmark { left: 120px; top: 118px; font-size: 60px; color: var(--white); }
  .card-back .wordmark-dot { width: 22px; height: 22px; background: var(--white); }
  .card-front .wordmark { left: 300px; top: 60px; font-size: 40px; color: var(--logo-grey); }
  .card-front .wordmark-dot { width: 16px; height: 16px; background: var(--blue-text); }

  .credentials {
    position: absolute;
    left: 0; right: 0; top: 268px;
    text-align: center;
    color: var(--white);
    font-size: 14px;
    line-height: 21px;
  }

  .contact { position: absolute; left: 46px; top: 48px; color: var(--ink); }
  .contact-name { font-size: 18px; font-weight: 700; color: var(--blue-text); letter-spacing: 0.5px; }
  .contact-title { font-size: 14px; color: var(--blue-text); margin-top: 2px; }
  .contact-lines { list-style: none; margin-top: 18px; font-size: 14.5px; line-height: 21px; }
  .contact-lines li { display: flex; align-items: center; gap: 5px; }
  .contact-lines svg { width: 14px; height: 14px; fill: none; stroke: var(--blue-text); stroke-width: 1.6; }

  .tagline-band {
    position: absolute;
    left: 0; right: 0; bottom: 0; height: 50px;
    background: linear-gradient(90deg, var(--blue-deep), var(--blue-mid) 50%, var(--blue-deep));
    color: var(--white);
    font-size: 15px;
    display: flex; align-items: center; justify-content: center;
    padding-left: 110px;
  }
</style>
</head>
<body>

<section class="card card-back">
  <svg class="card-decor" viewBox="0 0 530 320" aria-hidden="true">
    <defs>
      <linearGradient id="backPanel" x1="0" y1="0" x2="1" y2="1">
        <stop offset="0" stop-color="#0d3f94"/>
        <stop offset="1" stop-color="#14307a"/>
      </linearGradient>
    </defs>
    <polygon points="228,0 530,0 530,320" fill="url(#backPanel)"/>
    <polygon points="352,160 352,190 530,320" fill="#0a2560" opacity="0.7"/>
  </svg>
  <div class="wordmark"><span class="wordmark-dot"></span>VaroDine</div>
  <p class="credentials">Established in 1998<br>8(a)(w)(e), Cage #7KRT9, DUNS #462137580</p>
</section>

<section class="card card-front">
  <svg class="card-decor" viewBox="0 0 530 320" aria-hidden="true">
    <defs>
      <linearGradient id="frontPanel" x1="0" y1="0" x2="1" y2="0">
        <stop offset="0" stop-color="#c9cdec"/>
        <stop offset="1" stop-color="#ffffff"/>
      </linearGradient>
    </defs>
    <polygon points="235,0 530,0 530,285 470,285" fill="url(#frontPanel)"/>
    <polygon points="352,145 352,205 470,285" fill="#e2e2e2"/>
  </svg>
  <div class="wordmark"><span class="wordmark-dot"></span>VaroDine</div>

  <div class="contact">
    <h1 class="contact-name">DEREK HOLLOWAY</h1>
    <p class="contact-title">Vice President</p>
    <ul class="contact-lines">
      <li>5820 Birchmont Road</li>
      <li>Fallowby, FB 482917</li>
      <li><svg viewBox="0 0 14 14"><path d="M2 5c0-2 10-2 10 0v1H9V5H5v1H2z M3 7h8l1 5H2z"/></svg>555-318-2746 x 100</li>
      <li><svg viewBox="0 0 14 14"><path d="M2 5c0-2 10-2 10 0v1H9V5H5v1H2z M3 7h8l1 5H2z"/></svg>555-318-2746 Toll Free</li>
      <li><svg viewBox="0 0 14 14"><path d="M4 2h6v4H4z M2 6h10v6H2z M4 9h6"/></svg>555-902-6613</li>
      <li><svg viewBox="0 0 14 14"><path d="M1.5 3.5h11v7h-11z M1.5 3.5l5.5 4 5.5-4"/></svg>name@varodine.example</li>
      <li><svg viewBox="0 0 14 14"><circle cx="7" cy="7" r="5.5"/><path d="M1.5 7h11 M7 1.5c-3 3-3 8 0 11 M7 1.5c3 3 3 8 0 11"/></svg>www.varodine.example</li>
    </ul>
  </div>

  <div class="tagline-band">Connect • Collaborate • Achieve</div>
</section>

</body>
</html>
```